Design for online reviews widget

Attached is a wireframe of a widget we need designing to display reviews on websites from multiple sources. We need this provided at 3 different sizes including full screen, contained (like the wireframe) and mobile.
You have completely free rein on the styling.
The only elements that should remain untouched are the blue stars (https://www.filquarry.net/s/8vtmwp2291zq4h/kv%20stars.ai?dl=0) and powered by logo at the bottom.
Ignore the menu at the top of the wireframe, this is just from the website the widget will be placed on.
Businesses

```html
<!DOCTYPE html>
<html lang="en">
<head>
<meta charset="utf-8">
<title>Reviews Widget</title>
<link href="https://fonts.googleapis.com/css2?family=Nunito:wght@400;600;700;800&display=swap" rel="stylesheet">
<style>
  :root {
    --brand-blue: #35b6ea;
    --title-blue: #2b7fa9;
    --score-blue: #0b57a3;
    --card-bg: #f0f0f0;
    --text: #1e1e1e;
    --meta: #8c7352;
    --pill: #f7f7f7;
    --pill-text: #9a9a9a;
    --gold: #fbbc05;
    --green: #0a8c56;
    --rate-green: #20b573;
    --white: #ffffff;
  }
  * { box-sizing: border-box; margin: 0; padding: 0; }
  html, body { width: 763px; height: 1200px; overflow: hidden; background: var(--white); }
  body { font-family: "Nunito", sans-serif; color: var(--text); position: relative; }

  .summary-stars { position: absolute; top: 20px; left: 0; width: 763px; display: flex; justify-content: center; gap: 4px; }
  .summary-score { position: absolute; top: 60px; width: 763px; text-align: center; font-size: 10px; }
  .filter { position: absolute; top: 86px; left: 289px; width: 207px; height: 26px; border-radius: 13px; background: var(--pill); font-size: 9px; color: var(--pill-text); display: flex; align-items: center; justify-content: center; }
  .filter svg { position: absolute; right: 12px; top: 9px; }

  .review { position: absolute; left: 32px; width: 701px; background: var(--card-bg); border-radius: 6px; box-shadow: 0 2px 4px rgba(0,0,0,0.06); }
  .review-title { position: absolute; left: 20px; top: 18px; font-size: 14.5px; font-weight: 700; color: var(--title-blue); }
  .review-body { position: absolute; left: 20px; top: 51px; width: 500px; font-size: 9.5px; line-height: 22px; }
  .criteria { position: absolute; left: 21px; display: flex; font-size: 10px; }
  .criteria span { margin-right: 34px; }
  .criteria b, .service b { color: var(--title-blue); font-weight: 700; }
  .service { position: absolute; left: 21px; font-size: 10px; }
  .meta { position: absolute; left: 20px; font-size: 9.5px; font-weight: 700; color: var(--meta); }

  .source { position: absolute; right: 0; width: 230px; text-align: center; }
  .source-name { font-size: 22px; font-weight: 800; }
  .fixrate { color: #e0283a; }
  .searchly { color: #4285f4; font-size: 30px; }
  .listora { color: #111; font-size: 30px; }
  .ratewell { color: #11123a; font-size: 22px; }
  .stars-row { display: flex; justify-content: center; gap: 4px; margin-top: 10px; }

  .score-ring { position: absolute; left: 570px; top: 78px; }

  .load-more { position: absolute; left: 296px; top: 1105px; width: 173px; height: 37px; border-radius: 4px; background: var(--green); color: var(--white); font-size: 14px; font-weight: 800; display: flex; align-items: center; justify-content: center; }
  .powered { position: absolute; left: 635px; top: 1153px; font-size: 6.5px; }
  .powered-brand { position: absolute; left: 632px; top: 1168px; display: flex; align-items: center; gap: 4px; font-size: 11px; font-weight: 800; color: #222; }
  .powered-brand i { width: 20px; height: 20px; border-radius: 50%; background: var(--brand-blue); display: block; }
</style>
</head>
<body>
<svg width="0" height="0" style="position:absolute">
  <symbol id="star" viewBox="0 0 24 24"><path d="M12 2l2.9 6.6 7.1.6-5.4 4.7 1.6 7-6.2-3.7-6.2 3.7 1.6-7L2 9.2l7.1-.6z"/></symbol>
</svg>

<div class="summary-stars">
  <svg width="26" height="26" viewBox="0 0 26 26"><circle cx="13" cy="13" r="13" fill="var(--brand-blue)"/><use href="#star" x="5" y="5" width="16" height="16" fill="#fff"/></svg>
  <svg width="26" height="26" viewBox="0 0 26 26"><circle cx="13" cy="13" r="13" fill="var(--brand-blue)"/><use href="#star" x="5" y="5" width="16" height="16" fill="#fff"/></svg>
  <svg width="26" height="26" viewBox="0 0 26 26"><circle cx="13" cy="13" r="13" fill="var(--brand-blue)"/><use href="#star" x="5" y="5" width="16" height="16" fill="#fff"/></svg>
  <svg width="26" height="26" viewBox="0 0 26 26"><circle cx="13" cy="13" r="13" fill="var(--brand-blue)"/><use href="#star" x="5" y="5" width="16" height="16" fill="#fff"/></svg>
  <svg width="26" height="26" viewBox="0 0 26 26"><circle cx="13" cy="13" r="13" fill="var(--brand-blue)"/><use href="#star" x="5" y="5" width="16" height="16" fill="#fff"/></svg>
</div>
<div class="summary-score">Combined Review Score 4.3 out of 5</div>
<div class="filter">Filter Results
  <svg width="10" height="7" viewBox="0 0 10 7"><path d="M1 1l4 4 4-4" fill="none" stroke="var(--brand-blue)" stroke-width="1.5"/></svg>
</div>

<section class="review" style="top:134px;height:217px">
  <h2 class="review-title">Front Door With Windows Each Side And Side Window</h2>
  <p class="review-body">This is the second time we have used regent home Improvments , and the service is amazing! Martin came round several times as we keep changing our minds and he was so helpful and gave us good advice, and the guys who do the fitting are&nbsp; efficient and tidy . I’ve got to say the end result is amazing and I have recommended to many of friends . Thanks Regant</p>
  <div class="criteria" style="top:155px">
    <span><b>Reliablity:</b> 9.38</span><span><b>Courtesy:</b> 10</span><span><b>Tidiness:</b> 9.84</span><span><b>Workmanship:</b> 10</span>
  </div>
  <div class="meta" style="top:190px">Verified 28th September 2021 | Located In Brentwood</div>
  <div class="source" style="top:32px;right:8px"><div class="source-name fixrate">Fixrate</div></div>
  <svg class="score-ring" width="98" height="98" viewBox="0 0 98 98">
    <circle cx="49" cy="49" r="47" fill="var(--score-blue)"/>
    <circle cx="49" cy="49" r="41" fill="none" stroke="#fff" stroke-width="3"/>
    <circle cx="49" cy="49" r="37" fill="var(--score-blue)"/>
    <text x="49" y="59" text-anchor="middle" font-family="Nunito, sans-serif" font-weight="800" font-size="26" fill="#fff">9.77</text>
  </svg>
</section>

<section class="review" style="top:372px;height:221px">
  <h2 class="review-title">Positive: Professionalism, Quality, Value</h2>
  <p class="review-body">The team did a good job of replacing a large feature window spanning two floors, as well as the others in my property. They're a professional group who were willing to work out solutions to any problem, especially compared to other companies. Prices are fair, and my new UPVC windows look great. Special thanks to Frank for being so accommodating and for the good communication throughout.</p>
  <div class="service" style="top:156px"><b>Service:</b> Window installation</div>
  <div class="meta" style="top:188px">11 Months Ago By Daniel Hurst</div>
  <div class="source" style="top:48px;right:8px">
    <div class="source-name searchly">Searchly</div>
    <div class="stars-row" style="fill:var(--gold)">
      <svg width="20" height="20"><use href="#star"/></svg><svg width="20" height="20"><use href="#star"/></svg><svg width="20" height="20"><use href="#star"/></svg><svg width="20" height="20"><use href="#star"/></svg><svg width="20" height="20"><use href="#star"/></svg>
    </div>
  </div>
</section>

<section class="review" style="top:631px;height:204px">
  <h2 class="review-title">Brilliant All Round Professional, Friendly Service.</h2>
  <p class="review-body" style="width:480px">This home run friendly business was a real pleasure to deal with. From the professional, no pressure quote, nothing was too much trouble to ensure everything is as required for your needs with the quote and fitting. The workmanship and double glazing being fitted was brilliant and my home/outdoors was left tidy and clean leaving an outstanding impression for such an all round professional job. I would not hesitate to recommend this company, such a brilliant service from great hardworking people that care about their service.</p>
  <div class="meta" style="top:171px">13 Feb 2018 By GreenChair72</div>
  <div class="source" style="top:50px;right:14px">
    <div class="source-name listora">Listora</div>
    <div class="stars-row" style="fill:var(--gold)">
      <svg width="22" height="22"><use href="#star" width="22" height="22"/></svg><svg width="22" height="22"><use href="#star" width="22" height="22"/></svg><svg width="22" height="22"><use href="#star" width="22" height="22"/></svg><svg width="22" height="22"><use href="#star" width="22" height="22"/></svg><svg width="22" height="22"><use href="#star" width="22" height="22"/></svg>
    </div>
  </div>
</section>

<section class="review" style="top:869px;height:181px">
  <h2 class="review-title">Front Door With Windows Each Side And Side Window</h2>
  <p class="review-body" style="width:480px">This is the second time we have used regent home Improvments , and the service is amazing! Martin came round several times as we keep changing our minds and he was so helpful and gave us good advice, and the guys who do the fitting are&nbsp; efficient and tidy . I’ve got to say the end result is amazing and I have recommended to many of friends . Thanks Regant</p>
  <div class="meta" style="top:150px">13 Feb 2018 By Jo</div>
  <div class="source" style="top:50px;right:14px">
    <div class="source-name ratewell">Ratewell</div>
    <div class="stars-row" style="fill:var(--rate-green)">
      <svg width="20" height="20"><use href="#star"/></svg><svg width="20" height="20"><use href="#star"/></svg><svg width="20" height="20"><use href="#star"/></svg><svg width="20" height="20"><use href="#star"/></svg><svg width="20" height="20"><use href="#star"/></svg>
    </div>
  </div>
</section>

<div class="load-more">LOAD MORE</div>
<div class="powered">Powered by</div>
<div class="powered-brand"><i></i>ReviewWeave</div>
</body>
</html>
```